Creat new BusinessCard for Brightfold Consulting!

Hello Creativ Designer. I need a new Businesscard for our brand new Company "Brightfold Training". We do Consulting for a better Life & Work Situation. to create Fulfillment, Sense, Motivation and healthy Work Places in Company's. So we try to create a better World and help the employee to like what they do!
So we would like to have 2 Sites on the card. On the Back we want to put this words: "The sole meaning of life, is to serve humanity" (it can be vertical oder horizontal). In the front there is the Logo (Black or White) and Adress+ and Slogan.

Slogan on the front: -Make your Business & Life to a better place-

Name: Lukas Verhoff
Titel: Founder - Visionary - Trainer
Adress: Based in Switzerland

Tel: +41 (0) 71 583 42 17
Email: hello@brightfold-training.ch
Homepage: www.brightfold-training.ch

Thanks for your inspired Ideas and your help to make the world to a better place! IT has to be ready to print and normal Size.

Target Market(s)

insurance, Bank, Telecom, industry, IT, Medical

Contact Information for Business Card

Breite: 85 mm x Höhe: 55 mm

Colors

Designer to choose colors to be used in the design.

Requirements
Nice to have
• Thanks for your Ideas so far!
• Maybe you can try/play with the colors: Purple Code #652C8F and Grey #979797 from the Zelvor Logo purple and grey (but only a soft combination, not to much)

```html
<!DOCTYPE html>
<html lang="en">
<head>
<meta charset="utf-8">
<title>Brightfold Training – Business Card</title>
<link href="https://fonts.googleapis.com/css2?family=Open+Sans:wght@400;600;700&display=swap" rel="stylesheet">
<style>
  :root{
    --stage:#e9e7e4;
    --card:#151516;
    --card-edge:#0c0c0d;
    --ink:#ffffff;
    --ink-soft:#d9d9d9;
    --silver:#8d8d8f;
    --silver-dim:#6f6f72;
    --rule:#bdbdbd;
  }
  *{box-sizing:border-box;margin:0;padding:0}
  html,body{width:1200px;height:864px;overflow:hidden}
  body{
    background:var(--stage);
    font-family:"Open Sans",Arial,sans-serif;
    display:flex;align-items:center;justify-content:center;gap:40px;
  }
  .card{
    position:relative;width:540px;height:350px;background:var(--card);
    border-radius:4px;box-shadow:0 10px 30px rgba(0,0,0,.25);overflow:hidden;
  }
  /* back */
  .card--back .brand{
    position:absolute;left:0;right:0;top:110px;
    display:flex;flex-direction:column;align-items:center;gap:14px;
  }
  .brand__mark{width:62px;height:62px;border-radius:50%;background:var(--silver)}
  .card--back .brand__name{
    font-weight:700;font-size:26px;letter-spacing:.06em;text-transform:uppercase;color:var(--silver);
  }
  .card--back .motto{
    position:absolute;left:0;right:0;top:245px;text-align:center;
    font-size:15px;color:var(--silver-dim);letter-spacing:.01em;
  }
  /* front */
  .person{position:absolute;left:34px;top:118px}
  .person__name{font-weight:700;font-size:18px;color:var(--ink);text-transform:uppercase;letter-spacing:.01em}
  .person__title{font-size:13.5px;color:var(--ink-soft);text-transform:uppercase;margin-top:2px}
  .contact{list-style:none;margin-top:10px}
  .contact li{display:flex;align-items:center;gap:8px;font-size:13.5px;color:var(--ink-soft);line-height:21px}
  .contact svg{width:12px;height:12px;fill:var(--ink)}
  .card--front .brand{
    position:absolute;right:34px;top:112px;display:flex;align-items:center;gap:10px;
  }
  .card--front .brand__mark{width:44px;height:44px;background:var(--ink)}
  .card--front .brand__name{font-weight:700;font-size:17px;color:var(--ink);text-transform:uppercase;letter-spacing:.04em}
  .divider{position:absolute;left:34px;right:34px;top:250px;height:1px;background:var(--rule)}
  .slogan{
    position:absolute;right:34px;top:268px;font-weight:700;font-size:14px;color:var(--ink);
  }
</style>
</head>
<body>
  <section class="card card--back" aria-label="Card back">
    <div class="brand">
      <span class="brand__mark"></span>
      <span class="brand__name">Brightfold Training</span>
    </div>
    <p class="motto">The sole meaning of life, is to serve humanity</p>
  </section>

  <section class="card card--front" aria-label="Card front">
    <div class="person">
      <h1 class="person__name">Lukas Verhoff</h1>
      <p class="person__title">Founder - Visionary - Trainer</p>
      <ul class="contact">
        <li><svg viewBox="0 0 12 12"><path d="M2.5 1h2l1 3-1.3 1a6 6 0 0 0 2.8 2.8l1-1.3 3 1v2c0 .8-.6 1.5-1.5 1.5A9.5 9.5 0 0 1 1 2.5C1 1.6 1.7 1 2.5 1z"/></svg>+41 (0) 71 583 42 17</li>
        <li><svg viewBox="0 0 12 12"><path d="M0 2h12v8H0z M0 2l6 4 6-4" fill="none" stroke="#fff" stroke-width="1.4"/></svg>hello@brightfold-training.ch</li>
        <li><svg viewBox="0 0 12 12"><circle cx="6" cy="6" r="6"/></svg>www.brightfold-training.ch</li>
      </ul>
    </div>
    <div class="brand">
      <span class="brand__mark"></span>
      <span class="brand__name">Brightfold Training</span>
    </div>
    <div class="divider"></div>
    <p class="slogan">Make your Business &amp; Life to a better place</p>
  </section>
</body>
</html>
```